Design business card using existing logo.

PLEASE DO NOT USE "RED WHITE & BLACK" color combo! Thank you.

Try different color combos such as:
- Vintage colors like brown, orange, gold, blue (not all together but a combo of 1 or 3
- Blue, w/ grey, or silver or white, Blue monochromatic can work as well.
- Use monochromatic variations on back (just an idea)

- Include full name, "Quillmarsh Records" on at least one side.

Target Market(s)

Teens

Industry/Entity Type

Business

Colors
3277b5
ffc214
f04a50
f78f20

```html
<!DOCTYPE html>
<html lang="en">
<head>
<meta charset="utf-8">
<title>Quillmarsh Records — Business Card</title>
<link href="https://fonts.googleapis.com/css2?family=Montserrat:wght@400;500;600&display=swap" rel="stylesheet">
<style>
  :root {
    --backdrop: #2a2a2c;
    --card-navy: #2f4661;
    --card-navy-deep: #283c54;
    --card-ring: #3a5370;
    --silver: #d9dde2;
    --silver-soft: #aeb6c0;
    --white: #ffffff;
  }
  * { margin: 0; padding: 0; box-sizing: border-box; }
  html, body {
    width: 1200px; height: 900px; overflow: hidden;
    background: var(--backdrop);
    font-family: "Montserrat", sans-serif;
  }
  .canvas {
    position: relative; width: 1200px; height: 900px;
    display: flex; flex-direction: column; align-items: center;
    justify-content: center; gap: 40px;
  }
  .card {
    position: relative; width: 700px; height: 400px;
    border-radius: 28px; overflow: hidden;
    background: linear-gradient(135deg, var(--card-navy) 0%, var(--card-navy-deep) 100%);
  }
  .card-decor {
    position: absolute; border-radius: 50%;
    background: var(--card-ring);
    opacity: 0.45;
  }
  /* Front */
  .card-front .card-decor {
    width: 520px; height: 520px; left: 80px; top: -90px;
  }
  .front-wordmark {
    position: absolute; right: 60px; bottom: 120px;
    text-align: right; color: var(--silver);
  }
  .front-wordmark .brand-name {
    font-size: 34px; font-weight: 500; letter-spacing: 0.5px;
    padding-bottom: 6px; border-bottom: 1px solid var(--silver-soft);
  }
  .front-wordmark .brand-sub {
    font-size: 13px; font-weight: 500; letter-spacing: 9px;
    margin-top: 6px; margin-right: -9px; color: var(--silver-soft);
  }
  /* Back */
  .card-back .card-decor {
    width: 480px; height: 480px; left: -60px; top: 10px;
  }
  .back-brand {
    position: absolute; left: 110px; top: 110px;
    display: flex; flex-direction: column; align-items: center; gap: 18px;
  }
  .brand-dot {
    width: 100px; height: 100px; border-radius: 50%;
    background: var(--silver);
  }
  .back-brand .brand-name {
    font-size: 32px; font-weight: 500; color: var(--silver); letter-spacing: 0.5px;
  }
  .divider {
    position: absolute; left: 405px; top: 105px;
    width: 1px; height: 175px; background: var(--silver-soft);
  }
  .contact {
    position: absolute; left: 430px; top: 118px; color: var(--white);
  }
  .contact-name {
    font-size: 19px; font-weight: 600; letter-spacing: 0.5px; margin-bottom: 22px;
  }
  .contact-list { list-style: none; }
  .contact-item {
    display: flex; align-items: center; gap: 10px;
    font-size: 16px; font-weight: 500; margin-bottom: 8px;
  }
  .contact-icon { width: 14px; height: 14px; flex: none; }
</style>
</head>
<body>
<main class="canvas">
  <section class="card card-front">
    <div class="card-decor"></div>
    <div class="front-wordmark">
      <div class="brand-name">QUILLMARSH</div>
      <div class="brand-sub">RECORDS</div>
    </div>
  </section>

  <section class="card card-back">
    <div class="card-decor"></div>
    <div class="back-brand">
      <div class="brand-dot"></div>
      <div class="brand-name">QUILLMARSH</div>
    </div>
    <div class="divider"></div>
    <div class="contact">
      <div class="contact-name">DANIEL VERROW</div>
      <ul class="contact-list">
        <li class="contact-item">
          <svg class="contact-icon" viewBox="0 0 24 24" fill="#c8ced6"><path d="M6.6 10.8a15 15 0 0 0 6.6 6.6l2.2-2.2a1 1 0 0 1 1-.25 11.4 11.4 0 0 0 3.6.57 1 1 0 0 1 1 1V20a1 1 0 0 1-1 1A17 17 0 0 1 3 4a1 1 0 0 1 1-1h3.5a1 1 0 0 1 1 1c0 1.25.2 2.45.57 3.57a1 1 0 0 1-.25 1z"/></svg>
          555-014-2290
        </li>
        <li class="contact-item">
          <svg class="contact-icon" viewBox="0 0 24 24" fill="#c8ced6"><path d="M2 5h20v14H2z" fill="none" stroke="#c8ced6" stroke-width="2"/><path d="M2 5l10 8 10-8" fill="none" stroke="#c8ced6" stroke-width="2"/></svg>
          daniel@quillmarsh.com
        </li>
        <li class="contact-item">
          <svg class="contact-icon" viewBox="0 0 24 24" fill="none" stroke="#c8ced6" stroke-width="2"><circle cx="12" cy="12" r="10"/><path d="M2 12h20M12 2c3 3 3 17 0 20M12 2c-3 3-3 17 0 20"/></svg>
          www.quillmarsh.com
        </li>
      </ul>
    </div>
  </section>
</main>
</body>
</html>
```